Empowering Stationary for Fitness Business
Iron Harbor: Fitness and Trainings
Empowering Stationary for Fitness Business - Health
Creative Brief
Professional
Ned Farrow
Owner, Certified Personal Trainer
info@ironharborcoaching.example
www.ironharborcoaching.example
I am looking to have the following stationary items created: - business cards - folders - letter head - small note pads - postcard-sized flyer without the stamp area. ( On the front of the flyer please show the full attached logo centered and enlarged with the web address center closer to the bottom of the flyer. On the back please list: - where personal training meets small group trainings - indoor and outdoor weekend sessions - Strength Development - Muscle Stabilization - Functional Movement - Endurance. - team events and outings) - etc., any other examples you care to include Feel free to play around with any ideas.
Highlight the slogan of "Earn Every Rep, Every Day" in some way, near the top or bottom of the card. Please use a slightly different font to help it stand out. Please list the following points underneath the slogan with some space between : - where personal training meets small group trainings - indoor and outdoor weekend sessions - group events and outings

```html
<!DOCTYPE html>
<html lang="en">
<head>
<meta charset="utf-8">
<title>Iron Harbor – Stationery</title>
<link rel="stylesheet" href="https://fonts.googleapis.com/css2?family=Montserrat:wght@400;600;800&family=Oswald:wght@500&display=swap">
<style>
  :root {
    --bg: #ececec;
    --paper: #ffffff;
    --ink: #3a3a3a;
    --ink-soft: #6d6d6d;
    --band: #383838;
    --green: #4f7a3a;
    --ghost: #dcdcdc;
  }
  * { margin: 0; padding: 0; box-sizing: border-box; }
  html, body { width: 1200px; height: 936px; overflow: hidden; background: var(--bg); }
  body { position: relative; font-family: "Montserrat", Arial, sans-serif; color: var(--ink); }

  .sheet { position: absolute; background: var(--paper); box-shadow: 0 2px 6px rgba(0,0,0,.12); overflow: hidden; }

  .brand { display: flex; flex-direction: column; align-items: center; text-align: center; }
  .brand-mark { width: 14px; height: 14px; background: var(--ink); margin-bottom: 6px; }
  .brand-name { font-weight: 800; color: var(--ink); text-transform: uppercase; line-height: 1.1; white-space: nowrap; }
  .brand-sub { font-family: "Oswald", "Arial Narrow", sans-serif; font-weight: 500; color: var(--green); text-transform: uppercase; letter-spacing: .16em; white-space: nowrap; line-height: 1.3; }
  .brand-slogan { font-weight: 400; color: var(--ink-soft); text-transform: uppercase; letter-spacing: .2em; white-space: nowrap; }

  /* letterhead */
  .letterhead { left: 190px; top: 71px; width: 409px; height: 551px; }
  .letterhead .brand { position: absolute; left: 18px; top: 18px; align-items: flex-start; text-align: left; }
  .letterhead .brand-mark { width: 9px; height: 9px; margin-bottom: 3px; }
  .letterhead .brand-name { font-size: 8px; }
  .letterhead .brand-sub { font-size: 5.5px; }
  .letterhead .contact { position: absolute; left: 216px; top: 20px; font-size: 5.5px; line-height: 1.7; color: var(--ink-soft); }
  .letterhead .watermark { position: absolute; left: 0; right: 0; top: 255px; text-align: center; font-weight: 800; font-size: 38px; color: var(--ghost); text-transform: uppercase; }
  .letterhead .band-dark { position: absolute; left: 18px; right: 18px; bottom: 30px; height: 4px; background: var(--band); }
  .letterhead .band-green { position: absolute; left: 18px; right: 18px; bottom: 24px; height: 1px; background: var(--green); }

  /* folder */
  .folder { left: 634px; top: 38px; width: 388px; height: 586px; }
  .folder .line-top { position: absolute; left: 0; right: 0; top: 14px; height: 2px; background: #9a9a9a; }
  .folder .line-green { position: absolute; left: 0; right: 0; top: 18px; height: 1px; background: var(--green); }
  .folder .band-bottom { position: absolute; left: 0; right: 0; bottom: 14px; height: 6px; background: var(--band); }
  .folder .brand { position: absolute; left: 0; right: 0; top: 220px; }
  .folder .brand-mark { width: 22px; height: 22px; margin-bottom: 14px; }
  .folder .brand-name { font-size: 26px; }
  .folder .brand-sub { font-size: 14px; margin-top: 4px; }
  .folder .brand-slogan { font-size: 7px; margin-top: 4px; }

  /* business cards */
  .card-front { left: 36px; top: 655px; width: 139px; height: 116px; }
  .card-front .brand { position: absolute; left: 0; right: 0; top: 14px; }
  .card-front .brand-mark { width: 8px; height: 8px; margin-bottom: 3px; }
  .card-front .brand-name { font-size: 8px; }
  .card-front .brand-sub { font-size: 4.5px; }
  .card-front .contact { position: absolute; left: 0; right: 0; top: 62px; font-size: 4.5px; line-height: 1.7; color: var(--ink-soft); text-align: center; }

  .card-back { left: 36px; top: 786px; width: 139px; height: 117px; background: var(--band); color: #e6e6e6; }
  .card-back .person { position: absolute; left: 0; right: 0; top: 16px; text-align: center; }
  .card-back .person-name { font-size: 6.5px; font-weight: 600; letter-spacing: .1em; text-transform: uppercase; }
  .card-back .person-role { font-size: 4.5px; color: #bdbdbd; margin-top: 2px; }
  .card-back .services { position: absolute; left: 0; right: 0; top: 48px; text-align: center; font-size: 4.3px; line-height: 1.9; color: #cfcfcf; list-style: none; }

  /* envelope front */
  .envelope { left: 254px; top: 675px; width: 449px; height: 203px; }
  .envelope .band-top { position: absolute; left: 0; right: 0; top: 8px; height: 5px; background: var(--band); }
  .envelope .band-bottom { position: absolute; left: 0; right: 0; bottom: 14px; height: 6px; background: var(--band); }
  .envelope .brand { position: absolute; left: 20px; top: 24px; width: 130px; }
  .envelope .brand-mark { width: 9px; height: 9px; margin-bottom: 3px; }
  .envelope .brand-name { font-size: 9px; }
  .envelope .brand-sub { font-size: 5px; }

  /* envelope back */
  .envelope-back { left: 743px; top: 677px; width: 424px; height: 226px; }
  .envelope-back .flap { position: absolute; left: 0; right: 0; top: 0; height: 56px; background: var(--band); }
  .envelope-back .flap-url { position: absolute; left: 0; right: 0; top: 24px; text-align: center; font-size: 7px; letter-spacing: .2em; color: #e8e8e8; text-transform: uppercase; }
  .envelope-back .fold { position: absolute; left: 0; top: 56px; width: 424px; height: 170px; }
</style>
</head>
<body>

  <section class="sheet letterhead" aria-label="Letterhead">
    <div class="brand">
      <span class="brand-mark"></span>
      <span class="brand-name">Iron Harbor</span>
      <span class="brand-sub">Coaching &amp; Conditioning</span>
    </div>
    <div class="contact">
      <div>Tel: (555) 014-2290</div>
      <div>info@ironharborcoaching.example</div>
      <div>www.ironharborcoaching.example</div>
    </div>
    <div class="watermark">Iron Harbor</div>
    <div class="band-dark"></div>
    <div class="band-green"></div>
  </section>

  <section class="sheet folder" aria-label="Presentation folder">
    <div class="line-top"></div>
    <div class="line-green"></div>
    <div class="brand">
      <span class="brand-mark"></span>
      <span class="brand-name">Iron Harbor</span>
      <span class="brand-sub">Coaching &amp; Conditioning</span>
      <span class="brand-slogan">Earn Every Rep, Every Day</span>
    </div>
    <div class="band-bottom"></div>
  </section>

  <section class="sheet card-front" aria-label="Business card front">
    <div class="brand">
      <span class="brand-mark"></span>
      <span class="brand-name">Iron Harbor</span>
      <span class="brand-sub">Coaching &amp; Conditioning</span>
    </div>
    <div class="contact">
      <div>Ned Farrow</div>
      <div>Tel: (555) 014-2290</div>
      <div>info@ironharborcoaching.example</div>
    </div>
  </section>

  <section class="sheet card-back" aria-label="Business card back">
    <div class="person">
      <div class="person-name">Ned Farrow</div>
      <div class="person-role">Owner, Certified Personal Trainer</div>
    </div>
    <ul class="services">
      <li>Personal training meets small groups</li>
      <li>Indoor and outdoor weekend sessions</li>
      <li>Group events and outings</li>
    </ul>
  </section>

  <section class="sheet envelope" aria-label="Envelope front">
    <div class="band-top"></div>
    <div class="brand">
      <span class="brand-mark"></span>
      <span class="brand-name">Iron Harbor</span>
      <span class="brand-sub">Coaching &amp; Conditioning</span>
    </div>
    <div class="band-bottom"></div>
  </section>

  <section class="sheet envelope-back" aria-label="Envelope back">
    <div class="flap"></div>
    <div class="flap-url">www.ironharborcoaching.example</div>
    <svg class="fold" viewBox="0 0 424 170" aria-hidden="true">
      <polyline points="0,170 212,70 424,170" fill="none" stroke="#dddddd" stroke-width="1"/>
    </svg>
  </section>

</body>
</html>
```